Banner Design for Holistic Clinic

We need a banner to be designed for a Holistic Clinic which treats patient using IV Nutrition therapy, IV Vitamin C therapy, Chelation therapy, Homoepathy , Accupuncture, Ayurveda. Our website is www.verdantcarehub.in

We need the banner to show case all our services. IV Nutrition therapy, IV Vitamin C therapy, Chelation therapy, Homoepathy , Accupuncture, Ayurveda with special emphasis on IV Therapies. This will be in the front of the web page and will be used for leaflets and flex material.Ideally

I like the concept of IV infsuion bags, fruits etc. I have attached some of the pic which i liked. Please see the attachment "banner clinic july 13" But feel free to change it and bring in something better that will showcase all our services together

Target Market(s)

30 plus Adults

Industry/Entity Type

Health And Wellness

Font styles to use
Serif

Colors
acd036
f37122
33a6d7

Requirements
Must have
• Some samples are given below. It got to be colourful, yet pleasing.

```html
<!DOCTYPE html>
<html lang="en">
<head>
<meta charset="utf-8">
<title>Verdant Care Hub – Home</title>
<link href="https://fonts.googleapis.com/css2?family=Josefin+Sans:wght@400;600&family=Tinos:wght@700&display=swap" rel="stylesheet">
<style>
:root{
  --green:#acd036;
  --green-deep:#2f9a43;
  --green-band:#2c8f3c;
  --orange:#f37122;
  --red:#d9231d;
  --blue:#33a6d7;
  --ink:#222;
  --grey:#555;
  --white:#fff;
}
*{margin:0;padding:0;box-sizing:border-box}
html,body{width:1200px;height:1200px;overflow:hidden;background:var(--white)}
body{font-family:"Josefin Sans",sans-serif;color:var(--ink);position:relative}
.page{position:relative;width:1200px;height:1200px;overflow:hidden}

/* header */
.brand{position:absolute;left:111px;top:10px;width:305px}
.brand-doctor{font-size:9px;color:#444;letter-spacing:.3px;margin-left:46px}
.brand-row{display:flex;align-items:center;gap:10px;margin-top:2px}
.brand-square{width:36px;height:36px;background:var(--green)}
.brand-name{font-size:22px;font-weight:600;color:var(--green-deep);letter-spacing:.5px}
.brand-tag{font-size:8px;color:#444;margin-left:46px;margin-top:1px}
.phone{position:absolute;left:766px;top:18px;display:flex;align-items:center;gap:10px}
.phone-icon{width:36px;height:33px;background:var(--green);display:flex;align-items:center;justify-content:center}
.phone-text{font-size:21px;color:var(--ink);padding-top:4px}
.divider{position:absolute;left:116px;top:82px;width:954px;border-top:2px dashed #ddd}
.nav{position:absolute;top:96px;left:0;width:1200px;font-size:16px}
.nav a{position:absolute;color:var(--ink);text-decoration:none;white-space:nowrap}
.nav a.active{color:var(--red)}

/* hero */
.hero{position:absolute;left:0;top:120px;width:1200px;height:483px;
  background:radial-gradient(ellipse at 50% 45%,#fbfdf6 0%,#eef7dc 60%,#dcefbf 100%)}
.hero-leaves{position:absolute;left:0;bottom:0;width:1200px;height:135px;
  background:linear-gradient(180deg,rgba(172,208,54,0) 0%,#a9d04a 45%,#6fae2b 100%)}
.service{position:absolute;width:160px;text-align:center;transform:translateX(-50%)}
.service-photo{width:152px;height:152px;border-radius:50%;border:2px solid var(--green);padding:7px;margin:0 auto;background:var(--white)}
.service-photo span{display:block;width:100%;height:100%;border-radius:50%}
.service-label{font-family:"Tinos",serif;font-weight:700;font-size:17px;color:var(--orange);line-height:19px;margin-top:12px}
.service.low .service-label{margin-top:10px}

/* conditions */
.conditions{position:absolute;left:0;top:603px;width:1200px;height:375px;
  background:radial-gradient(ellipse at 30% 40%,#3aa04a 0%,var(--green-band) 70%,#27853a 100%);color:var(--white)}
.conditions h2{position:absolute;top:28px;width:100%;text-align:center;font-size:42px;font-weight:600;letter-spacing:.5px}
.condition-list{position:absolute;top:98px;list-style:none;font-size:15px;font-weight:600;width:220px}
.condition-list li{position:relative;padding-left:13px;line-height:19px;margin-bottom:11.7px}
.condition-list li::before{content:"";position:absolute;left:0;top:7px;width:3px;height:3px;border-radius:50%;background:var(--white)}

/* approach */
.approach-leaves{position:absolute;left:1081px;top:988px;width:130px;height:113px;border-radius:40% 10% 50% 30%;
  background:radial-gradient(circle at 60% 40%,#7fd13b,#3fa62a)}
.approach-art{position:absolute;left:150px;top:1020px;width:330px;height:180px;border-radius:40%;
  background:radial-gradient(ellipse at 50% 40%,#e2f1c6 0%,rgba(226,241,198,0) 70%)}
.approach-photo{position:absolute;left:195px;top:1128px;width:245px;height:110px;border-radius:14px;transform:rotate(4deg);
  background:linear-gradient(135deg,#1e8fcf,var(--blue))}
.approach h3{position:absolute;left:522px;top:1054px;width:520px;font-size:35px;font-weight:400;line-height:41px;color:var(--red)}
.approach h3 em{font-style:normal;color:var(--green-deep)}
.approach-rule{position:absolute;left:522px;top:1144px;width:86px;border-top:2px solid #ccc}
.approach p{position:absolute;left:522px;top:1178px;width:540px;font-size:13.5px;color:var(--grey);line-height:20px}
</style>
</head>
<body>
<div class="page">

  <header>
    <div class="brand">
      <div class="brand-doctor">Dr. Anna Verhoeven's (MBBS, MD)</div>
      <div class="brand-row">
        <span class="brand-square"></span>
        <span class="brand-name">VERDANT CARE HUB</span>
      </div>
      <div class="brand-tag">Allopathy, Ayurveda, Homeopathy, Acupuncture/Sujok</div>
    </div>
    <div class="phone">
      <span class="phone-icon">
        <svg width="12" height="18" viewBox="0 0 12 18"><rect x="1" y="1" width="10" height="16" rx="2" fill="none" stroke="#fff" stroke-width="2"/><circle cx="6" cy="14" r="1" fill="#fff"/></svg>
      </span>
      <span class="phone-text">9000 123 456, 8000 654 321</span>
    </div>
    <div class="divider"></div>
    <nav class="nav">
      <a class="active" href="#" style="left:297px">Home</a>
      <a href="#" style="left:377px">About us</a>
      <a href="#" style="left:479px">Services
        <svg width="9" height="6" viewBox="0 0 9 6"><path d="M1 1l3.5 3.5L8 1" fill="none" stroke="#222" stroke-width="1.3"/></svg></a>
      <a href="#" style="left:588px">Work with us</a>
      <a href="#" style="left:721px">Videos</a>
      <a href="#" style="left:806px">Contact us</a>
    </nav>
  </header>

  <section class="hero">
    <div class="hero-leaves" role="img" aria-label="Row of fresh green leaves along the bottom edge"></div>

    <div class="service" style="left:201px;top:40px">
      <div class="service-photo"><span role="img" aria-label="Assorted colourful vegetables and fruits" style="background:radial-gradient(circle at 40% 40%,#e8b33a,#c8452a 55%,#4d7d2c)"></span></div>
      <div class="service-label">IV NUTRITION<br>THERAPY</div>
    </div>
    <div class="service low" style="left:357px;top:174px">
      <div class="service-photo"><span role="img" aria-label="Sliced oranges" style="background:radial-gradient(circle at 45% 45%,#ffc24a,#f59a12 60%,#e07b0a)"></span></div>
      <div class="service-label">IV VITAMIN C<br>THERAPY</div>
    </div>
    <div class="service" style="left:518px;top:40px">
      <div class="service-photo"><span role="img" aria-label="Close view of red blood cells" style="background:radial-gradient(circle at 40% 40%,#e84a3a,#b8141a 60%,#7a0a0e)"></span></div>
      <div class="service-label" style="margin-top:14px">CHELATION<br>THERAPY</div>
    </div>
    <div class="service low" style="left:684px;top:174px">
      <div class="service-photo"><span role="img" aria-label="Amber bottle with spilled homoeopathic pills" style="background:radial-gradient(circle at 55% 55%,#e2c48a,#8a5a2a 55%,#3d5a2c)"></span></div>
      <div class="service-label">HOMOEPATHY</div>
    </div>
    <div class="service" style="left:858px;top:40px">
      <div class="service-photo"><span role="img" aria-label="Acupuncture needles placed on skin" style="background:radial-gradient(circle at 40% 50%,#f1d6c8,#e9e4ea 60%,#dfe5ef)"></span></div>
      <div class="service-label">ACCUPUNCTURE</div>
    </div>
    <div class="service low" style="left:1022px;top:174px">
      <div class="service-photo"><span role="img" aria-label="Herbal oils and mortar with leaves on bamboo mat" style="background:radial-gradient(circle at 50% 50%,#e9e2c5,#c79a3a 55%,#8a6a22)"></span></div>
      <div class="service-label" style="margin-top:16px">AYURVEDA</div>
    </div>
  </section>

  <section class="conditions" role="img" aria-label="Green grass background">
    <h2>Are you suffering from ?</h2>
    <ul class="condition-list" style="left:111px">
      <li>Cardio Vascular Diseaes</li><li>Menstrual Disorders</li><li>Stroke/Paralysis</li><li>Migraine</li>
      <li>Acidity</li><li>Muscular and Joint Pain</li><li>Arthiritis</li><li>Obesity</li>
    </ul>
    <ul class="condition-list" style="left:358px">
      <li>Astma</li><li>Parkinsonim</li><li>Back Ache</li><li>Prostrate Gland Enlasrgement</li>
      <li>Body Pain</li><li>Psoriasis</li><li>Cervical and Lumbar Spondylosis</li>
    </ul>
    <ul class="condition-list" style="left:605px">
      <li>Sciatica</li><li>Cramps</li><li>Sinsuitis</li><li>Disc slips and disc prolaps</li>
      <li>Snoring</li><li>Fibroid</li><li>Stress</li>
    </ul>
    <ul class="condition-list" style="left:852px">
      <li>Hypertension</li><li>Tennis Elbow</li><li>Insomnia</li><li>Thyroid Issues</li>
      <li>Kidney</li><li>Disorders</li><li>Ulcer</li>
    </ul>
  </section>

  <section class="approach">
    <div class="approach-leaves" role="img" aria-label="Sprig of fresh green leaves"></div>
    <div class="approach-art" role="img" aria-label="Soft green leaf illustration"></div>
    <div class="approach-photo" role="img" aria-label="Photo of a doctor in surgical cap"></div>
    <h3>We treat <em>holistically</em> using a combination of</h3>
    <div class="approach-rule"></div>
    <p>We are a "No SURGERY" centre dedicated to treating various diseases without Surgery. We treat holistically using a combination of</p>
  </section>

</div>
</body>
</html>
```